BOLD & MINIMALIST DESIGN NEEDED

We want a very bold but minimalistic business card design that is impactful and utilizes both sides of the business card. Our current logo is included for your use.

We want bold fonts and good use of negative space. We don't want the logo to overpower the design.

Target Market(s)

Professionals who are building new commercial buildings.

Industry/Entity Type

Construction

Contact Information for Business Card

Name, Title, email, office phone, cell phone, website

Font styles to use
Serif
Sans Serif

Requirements
Must have
• Bold design!

```html
<!DOCTYPE html>
<html lang="en">
<head>
<meta charset="utf-8">
<title>Ridgeline Design + Build — Business Card</title>
<link href="https://fonts.googleapis.com/css2?family=Montserrat:wght@400;500;700;800&display=swap" rel="stylesheet">
<style>
  :root {
    --green: #7dc242;
    --green-light: #a6d86c;
    --ink: #111111;
    --paper: #ffffff;
    --stage: #2b2b2b;
    --text: #1c1c1c;
  }
  * { margin: 0; padding: 0; box-sizing: border-box; }
  html, body { width: 1200px; height: 960px; overflow: hidden; }
  body { background: var(--stage); font-family: "Montserrat", sans-serif; position: relative; }

  .card {
    position: absolute;
    width: 700px; height: 400px;
    border-radius: 22px;
    overflow: hidden;
  }
  .card--front { left: 100px; top: 60px; background: var(--green); }
  .card--back { left: 400px; top: 500px; background: var(--paper); }

  .brand { font-weight: 800; text-transform: uppercase; line-height: 1; }
  .card--front .brand {
    position: absolute; inset: 0;
    display: flex; flex-direction: column; align-items: center; justify-content: center;
    color: var(--paper);
  }
  .card--front .brand__name { font-size: 76px; letter-spacing: 1px; }
  .card--front .brand__tag { font-size: 24px; letter-spacing: 10px; margin-top: 14px; }

  .card--back .brand {
    position: absolute; left: 40px; top: 115px; width: 280px;
    color: var(--ink); text-align: center;
  }
  .card--back .brand__name { font-size: 44px; }
  .card--back .brand__tag { font-size: 14px; letter-spacing: 6px; margin-top: 10px; }

  .divider {
    position: absolute; left: 350px; top: 78px;
    width: 2px; height: 160px; background: var(--green);
  }

  .contact { position: absolute; left: 380px; top: 66px; color: var(--text); }
  .contact__name { font-size: 30px; font-weight: 800; color: var(--green); text-transform: uppercase; line-height: 1.05; white-space: nowrap; }
  .contact__title { font-size: 16px; font-weight: 500; margin: 6px 0 12px; }
  .contact__list { list-style: none; }
  .contact__item { display: flex; align-items: center; gap: 12px; font-size: 16px; font-weight: 500; height: 28px; }
  .contact__item svg { width: 16px; height: 16px; flex: none; }

  .address {
    position: absolute; left: 0; right: 0; top: 280px;
    text-align: center; font-size: 17px; font-weight: 500; color: var(--text);
  }

  .band { position: absolute; left: 0; bottom: 0; width: 700px; height: 90px; }
</style>
</head>
<body>
  <section class="card card--front" aria-label="Card front">
    <div class="brand">
      <span class="brand__name">Ridgeline</span>
      <span class="brand__tag">Design + Build</span>
    </div>
  </section>

  <section class="card card--back" aria-label="Card back">
    <div class="brand">
      <div class="brand__name">Ridgeline</div>
      <div class="brand__tag">Design + Build</div>
    </div>

    <div class="divider"></div>

    <div class="contact">
      <div class="contact__name">Evan Stroud</div>
      <div class="contact__title">Managing Director</div>
      <ul class="contact__list">
        <li class="contact__item">
          <svg viewBox="0 0 24 24"><path fill="var(--green)" d="M6.6 10.8a15 15 0 0 0 6.6 6.6l2.2-2.2a1 1 0 0 1 1-.25 11.4 11.4 0 0 0 3.6.57 1 1 0 0 1 1 1V20a1 1 0 0 1-1 1A17 17 0 0 1 3 4a1 1 0 0 1 1-1h3.5a1 1 0 0 1 1 1c0 1.25.2 2.45.57 3.57a1 1 0 0 1-.25 1z"/></svg>
          555-214-7730
        </li>
        <li class="contact__item">
          <svg viewBox="0 0 24 24"><rect x="3" y="10" width="18" height="11" rx="2" fill="var(--green)"/><path d="M2 9c3-5 17-5 20 0l-3 2c-3-2-11-2-14 0z" fill="var(--green)"/></svg>
          000 000 0000
        </li>
        <li class="contact__item">
          <svg viewBox="0 0 24 24"><rect x="2" y="5" width="20" height="14" rx="1" fill="var(--green)"/><path d="M2 6l10 7 10-7" stroke="#fff" stroke-width="1.6" fill="none"/></svg>
          info@yourmail.com
        </li>
        <li class="contact__item">
          <svg viewBox="0 0 24 24"><circle cx="12" cy="12" r="10" fill="var(--green)"/><path d="M2 12h20M12 2c3 3 3 17 0 20M12 2c-3 3-3 17 0 20" stroke="#fff" stroke-width="1.3" fill="none"/></svg>
          www.yourwebsite.com
        </li>
      </ul>
    </div>

    <div class="address">480 Linden Ave, Ste 200, Austin, TX 78701</div>

    <svg class="band" viewBox="0 0 700 90" preserveAspectRatio="none" aria-hidden="true">
      <polygon points="0,62 478,62 452,90 0,90" fill="var(--ink)"/>
      <polygon points="478,62 496,20 700,20 700,90 452,90" fill="var(--green)"/>
    </svg>
  </section>
</body>
</html>
```